Velmora Commercial Finance Information Brochure

This brochure will be sent out to clients via A4 PDF on an email to showcase what our company has to offer. We are a commercial finance brokerage, that specialises in property finance. We would like to see designs following our colour scheme. The final design should demonstrate our professionalism and reliability.
I have attached our logo and also a few bullet points on our information and what we can offer. These can be slightly reworded for conciseness. Or leave the text sections as filler and I can fill these in.
I have also attached an overview of our colour scheme and design styling for your consideration.
Target Market(s)
Property Developers
Industry/Entity Type
Financial Services
Look and feel
Each slider illustrates characteristics of the customer's brand and the style your logo design should communicate.

```html
<!DOCTYPE html>
<html lang="en">
<head>
<meta charset="utf-8">
<title>Velmora Commercial Finance – Information Brochure</title>
<link rel="stylesheet" href="https://fonts.googleapis.com/css2?family=Montserrat:wght@400;500;800;900&family=Raleway:wght@400;500;600&display=swap">
<style>
:root{
  --blue:#0b3aa8;
  --green:#268a3a;
  --green-light:#8dc63f;
  --green-mid:#4aa83a;
  --ink:#1b1b1b;
  --panel:#f4f4f4;
  --page:#ffffff;
  --backdrop:#ececec;
}
*{margin:0;padding:0;box-sizing:border-box}
html,body{width:1200px;height:2403px;overflow:hidden;background:var(--backdrop)}
.flyer{
  position:absolute;left:60px;top:438px;width:1009px;height:1427px;
  background:var(--page);transform:scale(1.0704);transform-origin:top left;
  box-shadow:0 10px 30px rgba(0,0,0,.18);overflow:hidden;
  font-family:"Raleway",sans-serif;color:var(--ink);
}
.brand{position:absolute;left:64px;top:80px;display:flex;align-items:center;gap:18px}
.brand-mark{width:34px;height:34px;background:var(--green)}
.brand-name{font-family:"Raleway",sans-serif;font-weight:600;font-size:58px;color:var(--blue);letter-spacing:1px;line-height:1}
.intro-band{position:absolute;left:0;top:218px;width:1009px;height:392px;background:var(--blue)}
.intro-text{position:absolute;left:64px;top:272px;width:500px;color:#fff;font-size:25.5px;line-height:34.6px;letter-spacing:-.5px}
.portrait-panel{position:absolute;left:610px;top:0;width:340px;height:652px;background:linear-gradient(180deg,var(--green-light),var(--green-mid))}
.portrait{position:absolute;left:0;top:40px;width:340px;height:612px;background:linear-gradient(180deg,rgba(200,215,235,.0) 0%,rgba(190,208,232,.55) 35%,rgba(170,195,228,.7) 100%)}
.body-copy{position:absolute;left:64px;width:860px;font-size:25.5px;line-height:34.6px;letter-spacing:-.5px}
.body-copy.one{top:664px}
.body-copy.two{top:783px;width:720px}
.goal-box{position:absolute;left:40px;top:917px;width:602px;height:156px;background:var(--green);padding:14px 0 0 24px}
.goal-box h2{font-family:"Montserrat",sans-serif;font-weight:900;font-size:43px;line-height:42px;color:#fff;text-transform:uppercase;letter-spacing:-.3px}
.growth-box{position:absolute;left:649px;top:917px;width:323px;height:156px;background:var(--blue)}
.growth-art{position:absolute;left:660px;top:795px;width:312px;height:290px;background:radial-gradient(ellipse at 55% 65%,rgba(222,180,150,.55),rgba(80,110,190,0) 70%)}
.cta-panel{position:absolute;left:42px;top:1078px;width:527px;height:249px;background:var(--panel);padding:22px 0 0 22px}
.cta-panel p{font-size:30px;line-height:40.5px;font-weight:400;letter-spacing:-.4px}
.cta-panel .cta-strong{margin-top:10px;font-weight:600;letter-spacing:-.8px}
.contact{position:absolute;left:585px;top:1090px;font-family:"Montserrat",sans-serif;font-size:24.5px;line-height:34.5px}
.contact address{font-style:normal;margin-bottom:13px}
.contact ul{list-style:none}
.contact li{display:flex;align-items:center;gap:14px;height:36.5px}
.contact svg{width:22px;height:22px;flex:none}
.footer-wave{position:absolute;left:0;bottom:0;width:1009px;height:100px}
</style>
</head>
<body>
<article class="flyer">
  <div class="intro-band"></div>
  <div class="brand"><span class="brand-mark"></span><span class="brand-name">Velmora Finance</span></div>
  <p class="intro-text">Velmora Commercial Finance understands the frustrations and inefficiencies of today's market. As former lenders and developers, we've experienced the challenges of tight deadlines and information gathering. That's why we founded Velmora Finance – to provide efficient and reliable connections between developers and lenders.</p>
  <div class="portrait-panel">
    <div class="portrait" role="img" aria-label="Smiling advisor in a light blue shirt writing on a clipboard"></div>
  </div>
  <p class="body-copy one">With streamlined processes, we ensure clear and swift communication throughout the financing journey. From initial consultation to final funding, we guide you for a smooth experience.</p>
  <p class="body-copy two">Drawing on our extensive asset management background, we have a strong network of fund managers, institutions, UHNWI, and private equity lenders for non-traditional financing options.</p>
  <div class="goal-box"><h2>Our goal is to secure the best solutions quickly &amp; effectively.</h2></div>
  <div class="growth-box"></div>
  <div class="growth-art" role="img" aria-label="Open hand holding a rising bar chart with a green upward arrow"></div>
  <div class="cta-panel">
    <p>Choose Velmora Commercial Finance for efficient and reliable property finance.</p>
    <p class="cta-strong">Contact us today to achieve your financial goals.</p>
  </div>
  <div class="contact">
    <address>2150 Birchwood Lane<br>Fairbanks, Alaska 99701</address>
    <ul>
      <li><svg viewBox="0 0 24 24"><path fill="#268a3a" d="M6.6 10.8a15 15 0 0 0 6.6 6.6l2.2-2.2c.3-.3.7-.4 1-.2 1.1.4 2.3.6 3.6.6.6 0 1 .4 1 1V20c0 .6-.4 1-1 1A17 17 0 0 1 3 4c0-.6.4-1 1-1h3.5c.6 0 1 .4 1 1 0 1.3.2 2.5.6 3.6.1.3 0 .7-.2 1z"/></svg>555-201-4873</li>
      <li><svg viewBox="0 0 24 24"><rect x="6" y="2" width="12" height="20" rx="2" fill="none" stroke="#268a3a" stroke-width="2.4"/><circle cx="12" cy="18" r="1.3" fill="#268a3a"/></svg>555-309-6612</li>
      <li><svg viewBox="0 0 24 24"><rect x="2" y="5" width="20" height="14" fill="#268a3a"/><path d="M2 5l10 8 10-8" fill="none" stroke="#fff" stroke-width="1.6"/></svg>info@velmorafinance.com</li>
      <li><svg viewBox="0 0 24 24"><circle cx="12" cy="12" r="10" fill="#268a3a"/><path d="M2 12h20M12 2c3 3 3 17 0 20M12 2c-3 3-3 17 0 20" fill="none" stroke="#fff" stroke-width="1.3"/></svg>www.velmorafinance.com</li>
    </ul>
  </div>
  <svg class="footer-wave" viewBox="0 0 1009 100" preserveAspectRatio="none" aria-hidden="true">
    <path d="M0 30 Q500 48 1009 0 L1009 100 L0 100Z" fill="#268a3a"/>
    <path d="M0 40 Q500 52 1009 14 L1009 100 L0 100Z" fill="#0b3aa8"/>
  </svg>
</article>
</body>
</html>
```